We need a design for our retail display and for our stockist's retail display.
Our product is fresh corn tortillas. These can be used to make tacos, quesadillas, tortilla chips and tostadas.
We want the table talker to use our brand style (see our website) and show the tortillas versatility.
verdel-foods.co.uk
It should also have a space for our stockists to write in a blank space under the heading "Our fresh tortillas are delivered every....[blank space]"
The table talker should be 75mm tall x 150mm wide. This will also have a 25mm self adhesive flap at the top which can be blank or the same colour as the background.
Please feel free to use any files from our website as well as illustrations attached.
Customers in high end shops and delis
food and drink

```html
<!DOCTYPE html>
<html lang="en">
<head>
<meta charset="utf-8">
<title>Verdel – Table Talker</title>
<link rel="stylesheet" href="https://fonts.googleapis.com/css2?family=Fredoka:wght@600&family=Oswald:wght@500&display=swap">
<style>
  :root {
    --navy: #1e2c44;
    --navy-line: #34435c;
    --yellow: #e8c121;
    --white: #ffffff;
    --page: #e6e6e6;
  }
  html, body {
    margin: 0;
    width: 1200px;
    height: 672px;
    overflow: hidden;
    background: var(--page);
  }
  .canvas {
    position: relative;
    width: 1200px;
    height: 672px;
  }
  .table-talker {
    position: absolute;
    left: 54px;
    top: 62px;
    width: 1092px;
    height: 547px;
    display: block;
  }
  .panel-navy { fill: var(--navy); }
  .panel-yellow { fill: var(--yellow); }
  .flap-fold { stroke: var(--navy-line); stroke-width: 1.5; }
  .brand-disc { fill: var(--navy); stroke: var(--yellow); stroke-width: 3; }
  .brand-name {
    font-family: "Fredoka", sans-serif;
    font-weight: 600;
    font-size: 46px;
    fill: var(--yellow);
  }
  .headline {
    font-family: "Fredoka", sans-serif;
    font-weight: 600;
    font-size: 64px;
    fill: var(--yellow);
  }
  .write-in-banner { fill: var(--white); }
  .write-in-label {
    font-family: "Fredoka", sans-serif;
    font-weight: 600;
    font-size: 64px;
    fill: var(--navy);
  }
  .claim-badge { fill: var(--navy); stroke: var(--yellow); stroke-width: 1.5; }
  .website {
    font-family: "Oswald", sans-serif;
    font-weight: 500;
    font-size: 17px;
    letter-spacing: 0.5px;
    fill: var(--navy);
  }
</style>
</head>
<body>
<div class="canvas">
  <svg class="table-talker" viewBox="0 0 910 456" xmlns="http://www.w3.org/2000/svg" aria-label="Verdel fresh tortillas table talker">
    <!-- adhesive flap -->
    <rect class="panel-navy" x="0" y="0" width="910" height="152"/>
    <line class="flap-fold" x1="0" y1="152" x2="910" y2="152"/>

    <!-- front face -->
    <rect class="panel-navy" x="0" y="152" width="910" height="304"/>
    <polygon class="panel-yellow" points="0,288 290,288 352,393 910,393 910,456 0,456"/>

    <!-- brand mark -->
    <circle class="brand-disc" cx="165" cy="278" r="94"/>
    <text class="brand-name" x="165" y="294" text-anchor="middle">Verdel</text>

    <!-- heading -->
    <text class="headline" x="600" y="240" text-anchor="middle" textLength="575" lengthAdjust="spacingAndGlyphs">Our fresh Tortillas</text>
    <text class="headline" x="600" y="305" text-anchor="middle" textLength="406" lengthAdjust="spacingAndGlyphs">are Delivered</text>

    <!-- stockist write-in area -->
    <polygon class="write-in-banner" points="330,330 870,330 830,406 370,406"/>
    <text class="write-in-label" x="600" y="388" text-anchor="middle" textLength="220" lengthAdjust="spacingAndGlyphs">Every...</text>

    <!-- product claim badges -->
    <g class="claims">
      <circle class="claim-badge" cx="58" cy="412" r="24"/>
      <circle class="claim-badge" cx="113" cy="412" r="24"/>
      <circle class="claim-badge" cx="167" cy="412" r="24"/>
      <circle class="claim-badge" cx="222" cy="412" r="24"/>
      <circle class="claim-badge" cx="276" cy="412" r="24"/>
    </g>

    <!-- website -->
    <text class="website" x="600" y="436" text-anchor="middle" textLength="411" lengthAdjust="spacingAndGlyphs">FOR MORE INFO VISIT: WW.VERDEL-FOODS.CO.UK</text>
  </svg>
</div>
</body>
</html>
```